Business Card for new Overseas Property Buying Business

Hi

We need a new business card for our new business.

We are Faraway Nest Finders. So we search locations on behalf of our clients to find them the ideal home.

These are mainly holiday homes in nice locations - but sometimes people are looking to relocate.

I am looking for a nice simple design - that has some class and professionalism about it. Taking inspiration from our logo.

Text wise I was thinking of maybe having something like. (THE FONT FOR THIS SHOULD BE LIKE THE WRITING IN THE ATTACHMENT WITH THE MAP ON IT)

1)
What does your dream house have (tick all that apply):
swimming pool x
private vineyard x
herb garden x
full sized football pitch x

2)
How to buy a home abroad:

Method 1:
1) Scour internet for suitable estate agents
2) Arrange hectic holiday timetable with multiple agents in multiple languages
3) Fly to destination to find property was not as it seemed
4) Feel frustrated and helpless
OR
Method 2:
Contact your expert home hunter (details overleaf) - and leave the hard work to them

The end result should give people confidence that they are dealing with a professional organisation - and feel like they can place their trust in them. I would want it to drive them to either contact us directly or visit the website.

Please include name (Gordon Tramley), position (founder), contact numbers x 2, email address, website (www.quelvatrix-moor.com)

I look forward to seeing your entries.

Reason: Hi Sorry to extend - Xmas has got in the way of my plans. I will be providing feedback. Happy Christmas to you all.

```html
<!DOCTYPE html>
<html lang="en">
<head>
<meta charset="utf-8">
<title>Quelvatrix &amp; Moor — Business Card</title>
<link href="https://fonts.googleapis.com/css2?family=Old+Standard+TT:wght@400;700&family=Nothing+You+Could+Do&display=swap" rel="stylesheet">
<style>
  :root {
    --stage: #d9d9d9;
    --card-white: #ffffff;
    --ink-brown: #4a3b30;
    --accent-orange: #e0603a;
    --compass-ring: #e5714a;
    --faint-ring: #f3d9c9;
    --parchment-light: #eadcb8;
    --parchment-mid: #d9b67a;
    --parchment-dark: #b9824a;
    --land-green: #8fb14a;
    --land-yellow: #e5c93c;
    --script-ink: #1f1a16;
  }
  * { box-sizing: border-box; margin: 0; padding: 0; }
  html, body { width: 1200px; height: 900px; overflow: hidden; }
  body {
    background: var(--stage);
    position: relative;
    font-family: "Old Standard TT", Georgia, serif;
    color: var(--ink-brown);
  }
  .card {
    position: absolute;
    left: 250px;
    width: 700px;
    height: 400px;
    overflow: hidden;
    box-shadow: 0 6px 18px rgba(0,0,0,.25);
  }
  .card--front { top: 40px; background: var(--card-white); }
  .card--back { top: 470px; }

  /* front */
  .front__watermark {
    position: absolute;
    right: -70px; top: 20px;
    width: 380px; height: 380px;
    border-radius: 50%;
    background: var(--faint-ring);
    opacity: .7;
  }
  .brand {
    position: absolute;
    left: 40px; top: 70px;
    width: 330px;
    text-align: center;
  }
  .brand__mark {
    width: 150px; height: 150px;
    margin: 0 auto 22px;
    border-radius: 50%;
    background: var(--compass-ring);
  }
  .brand__name {
    font-size: 42px;
    font-weight: 400;
    line-height: 1;
    padding-bottom: 6px;
    border-bottom: 2px solid var(--ink-brown);
  }
  .brand__tagline {
    font-size: 20px;
    font-weight: 700;
    letter-spacing: 1px;
    margin-top: 6px;
  }
  .contact {
    position: absolute;
    left: 390px; top: 48px;
  }
  .contact__name {
    font-size: 24px;
    font-weight: 700;
    letter-spacing: .5px;
    text-transform: uppercase;
  }
  .contact__role {
    font-size: 17px;
    color: var(--accent-orange);
    margin-bottom: 6px;
  }
  .contact__list { list-style: none; font-size: 16px; }
  .contact__item {
    display: flex; align-items: center; gap: 8px;
    height: 26px;
  }
  .contact__icon { width: 16px; height: 16px; flex: none; }

  /* back */
  .back__map {
    position: absolute; inset: 0;
    background:
      radial-gradient(ellipse 30% 35% at 32% 35%, var(--land-yellow), transparent 70%),
      radial-gradient(ellipse 22% 40% at 62% 55%, var(--land-green), transparent 70%),
      radial-gradient(ellipse 35% 30% at 82% 25%, #e29a3a, transparent 70%),
      linear-gradient(135deg, var(--parchment-light), var(--parchment-mid) 55%, var(--parchment-dark));
  }
  .back__seal {
    position: absolute;
    left: 10px; top: 150px;
    width: 120px; height: 120px;
    border-radius: 50%;
    background: var(--compass-ring);
    opacity: .45;
  }
  .back__slogan {
    position: absolute;
    left: 200px; top: 40px;
    font-family: "Nothing You Could Do", cursive;
    font-size: 40px;
    color: var(--script-ink);
    letter-spacing: 6px;
    transform: rotate(14deg);
    transform-origin: left top;
    white-space: nowrap;
  }
  .back__brand {
    position: absolute;
    right: 90px; bottom: 60px;
    font-size: 26px;
    color: var(--ink-brown);
    opacity: .35;
  }
</style>
</head>
<body>

  <section class="card card--front">
    <div class="front__watermark" aria-hidden="true"></div>

    <div class="brand">
      <div class="brand__mark" aria-hidden="true"></div>
      <h1 class="brand__name">Quelvatrix &amp; Moor</h1>
      <p class="brand__tagline">FARAWAY NEST FINDERS</p>
    </div>

    <div class="contact">
      <h2 class="contact__name">Gordon Tramley</h2>
      <p class="contact__role">founder</p>
      <ul class="contact__list">
        <li class="contact__item">
          <svg class="contact__icon" viewBox="0 0 16 16" aria-hidden="true"><circle cx="8" cy="8" r="7" fill="none" stroke="currentColor"/><path d="M5 4.5l1.5 0 .8 2-1 .8a5 5 0 0 0 2.4 2.4l.8-1 2 .8v1.5c-3.5.3-6.8-3-6.5-6.5z" fill="currentColor"/></svg>
          555 017 230 | 555 017 231
        </li>
        <li class="contact__item">
          <svg class="contact__icon" viewBox="0 0 16 16" aria-hidden="true"><circle cx="8" cy="8" r="7" fill="none" stroke="currentColor"/><rect x="4" y="5.5" width="8" height="5" fill="none" stroke="currentColor"/><path d="M4 5.5l4 3 4-3" fill="none" stroke="currentColor"/></svg>
          quelvatrix&amp;moor@mail.com
        </li>
        <li class="contact__item">
          <svg class="contact__icon" viewBox="0 0 16 16" aria-hidden="true"><circle cx="8" cy="8" r="7" fill="none" stroke="currentColor"/><ellipse cx="8" cy="8" rx="3" ry="7" fill="none" stroke="currentColor"/><path d="M1 8h14M2.5 4.5h11M2.5 11.5h11" stroke="currentColor" fill="none"/></svg>
          www.quelvatrix-moor.com
        </li>
      </ul>
    </div>
  </section>

  <section class="card card--back">
    <div class="back__map" role="img" aria-label="Vintage parchment world map with colourful countries"></div>
    <div class="back__seal" aria-hidden="true"></div>
    <p class="back__slogan">Start the adventure</p>
    <p class="back__brand">Quelvatrix &amp; Moor</p>
  </section>

</body>
</html>
```